Veltora Solar business cards for gerald pashwick

Need a solar business card designed. I sell solar systems to home owners. Company’s name is Veltora solar. I want the business card to have this.
Veltora Solar
Gerald Pashwick
210.555.0147
Solar consultant
Gpashwick@veltorasolar.example
I would like the card to be black and green with the veltora logo on it if possible. If it’s possible to make atleast one of the designs green background with black lettering I would like to see that.
No upfront cost! Start saving today!
Target Market(s)
Residential home owners
Industry/Entity Type
Solar Energy
Contact Information for Business Card
Veltora Solar
Gerald Pashwick
210.555.0147
Solar consultant
Gpashwick@veltorasolar.example
Also if it would look better by adding in one of these that would be fine.

```html
<!DOCTYPE html>
<html lang="en">
<head>
<meta charset="utf-8">
<title>Veltora Solar business cards – Gerald Pashwick</title>
<link rel="stylesheet" href="https://fonts.googleapis.com/css2?family=Lato:wght@400;700&family=Montserrat:wght@500&display=swap">
<style>
  :root {
    --stage: #2b2b2b;
    --card-dark: #242424;
    --brand-green: #6cc43a;
    --green-top: #3db548;
    --green-bottom: #8cc940;
    --ink: #1e2a1c;
    --white: #ffffff;
  }
  * { margin: 0; padding: 0; box-sizing: border-box; }
  html, body { width: 1200px; height: 901px; overflow: hidden; }
  body {
    background: var(--stage);
    position: relative;
    font-family: "Lato", sans-serif;
  }
  .card {
    position: absolute;
    width: 560px;
    height: 320px;
    border-radius: 3px;
    box-shadow: 0 10px 28px rgba(0,0,0,0.45);
    overflow: hidden;
  }
  /* Back side */
  .card-back { left: 60px; top: 90px; background: var(--card-dark); }
  .card-back .brand-name {
    position: absolute; left: 0; right: 0; top: 105px;
    text-align: center;
    font-family: "Montserrat", sans-serif; font-weight: 500;
    font-size: 38px; letter-spacing: 1px;
    color: var(--brand-green);
  }
  .card-back .brand-name .dot {
    display: inline-block; width: 14px; height: 14px; border-radius: 50%;
    background: var(--brand-green); margin-right: 12px; vertical-align: middle;
  }
  .card-back .web-rule {
    position: absolute; left: 0; right: 0; top: 228px;
    display: flex; align-items: center; gap: 10px;
  }
  .card-back .web-rule::before,
  .card-back .web-rule::after {
    content: ""; flex: 1; height: 1px; background: var(--brand-green);
  }
  .card-back .website { font-size: 12px; color: var(--brand-green); letter-spacing: .3px; }

  /* Front side */
  .card-front {
    left: 580px; top: 490px;
    background: linear-gradient(160deg, var(--green-top) 0%, var(--green-bottom) 100%);
  }
  .card-front .brand-name {
    position: absolute; left: 34px; top: 34px;
    font-family: "Montserrat", sans-serif; font-weight: 500;
    font-size: 26px; color: var(--white); letter-spacing: .5px;
  }
  .card-front .accent-rule {
    position: absolute; left: 34px; right: 26px; top: 176px;
    height: 2px; background: var(--ink);
  }
  .card-front .contact {
    position: absolute; left: 34px; top: 140px; color: var(--ink);
  }
  .contact .person { font-size: 28px; font-weight: 400; line-height: 1; }
  .contact .role { font-size: 14px; margin-top: 18px; }
  .contact .company {
    font-size: 13px; margin-top: 12px; padding-top: 6px;
    border-top: 1px solid var(--ink); display: inline-block;
  }
  .contact .detail {
    display: flex; align-items: center; gap: 8px;
    font-size: 13px; margin-top: 10px;
  }
  .contact .detail svg { width: 14px; height: 14px; flex: none; }
</style>
</head>
<body>
  <section class="card card-back" aria-label="Card back">
    <div class="brand-name"><span class="dot"></span>Veltora Solar</div>
    <div class="web-rule"><span class="website">www.veltorasolar.example</span></div>
  </section>

  <section class="card card-front" aria-label="Card front">
    <div class="brand-name">Veltora Solar</div>
    <div class="accent-rule"></div>
    <div class="contact">
      <p class="person">Gerald Pashwick</p>
      <p class="role">Solar consultant</p>
      <p class="company">Veltora.Solar</p>
      <p class="detail">
        <svg viewBox="0 0 16 16" aria-hidden="true"><circle cx="8" cy="8" r="7" fill="none" stroke="#ffffff" stroke-width="1.2"/><path d="M5.5 4.5l1.3 1.6-.7.9c.5 1 1.2 1.7 2.2 2.2l.9-.7 1.6 1.3-.8 1.2C7.5 10.8 5.2 8.5 4.3 5.3z" fill="#ffffff"/></svg>
        <span>210.555.0147</span>
      </p>
      <p class="detail">
        <svg viewBox="0 0 16 16" aria-hidden="true"><rect x="1.5" y="3.5" width="13" height="9" fill="none" stroke="#ffffff" stroke-width="1.2"/><path d="M1.5 3.5L8 9l6.5-5.5" fill="none" stroke="#ffffff" stroke-width="1.2"/></svg>
        <span>Gpashwick@veltorasolar.example</span>
      </p>
    </div>
  </section>
</body>
</html>
```